Law firm business card

Information:

Me Marisa Delacourt

website: velmont-juris.ca
email: marisa@velmont-juris.ca
Phone: 514 372-5106
Fax: 514 372-5107

Address:
Delacourt and associates
2917 Brisebois
Montreal, QC
H3K 2T9

Areas of Expertise:
Franchise Agreements, Financing, Acquisition, Real Estate Development, Commercial Agreements and Corporate Law

Target Market(s)

executives, companie managers

Industry/Entity Type

Business

Colors
f78f20
000000

Requirements
Must have
• Must use the logo, the logo is available here:

https://www.filevault-share.net/sh/qe82kd0pl1m7/BXtr9LmQw3zPaYkN

```html
<!DOCTYPE html>
<html lang="en">
<head>
<meta charset="utf-8">
<title>Delacourt &amp; Associates – Business Card</title>
<link rel="stylesheet" href="https://fonts.googleapis.com/css2?family=Gelasio:wght@400;700&family=Noto+Sans:wght@400&display=swap">
<style>
  :root {
    --brand-orange: #f78f20;
    --brand-grey: #58585a;
    --ink-dark: #4a4a4c;
    --paper: #ffffff;
    --backdrop: #2b2b2b;
    --serif: "Gelasio", Georgia, serif;
    --sans: "Noto Sans", Verdana, sans-serif;
  }
  * { box-sizing: border-box; margin: 0; padding: 0; }
  html, body { width: 1200px; height: 900px; overflow: hidden; }
  body { background: var(--backdrop); position: relative; font-family: var(--serif); }

  .card {
    position: absolute;
    width: 620px;
    height: 355px;
    overflow: hidden;
    box-shadow: 0 10px 30px rgba(0,0,0,.45);
  }

  /* Back of card */
  .card--back {
    left: 110px; top: 110px;
    background: var(--brand-orange);
  }
  .back-brand {
    position: absolute;
    left: 48px; top: 60px;
    width: 240px;
    text-align: center;
    color: var(--paper);
  }
  .back-brand__mark {
    display: block;
    width: 150px; height: 150px;
    margin: 0 auto 22px;
    border: 5px solid var(--paper);
    border-radius: 50%;
  }
  .back-brand__name {
    font-family: var(--serif);
    font-weight: 400;
    font-size: 30px;
    letter-spacing: 2px;
    line-height: 1.1;
    text-transform: uppercase;
  }
  .back-brand__name small { display: block; font-size: 16px; letter-spacing: 4px; }

  .expertise {
    position: absolute;
    right: 40px; top: 70px;
    width: 268px;
    padding: 26px 18px 24px 22px;
    background: var(--paper);
    border-radius: 22px;
    box-shadow: 0 4px 8px rgba(0,0,0,.25);
    list-style: none;
    color: var(--ink-dark);
    font-size: 20px;
    line-height: 1.15;
  }

  /* Front of card */
  .card--front {
    left: 470px; top: 410px;
    background: var(--paper);
  }
  .front-brand {
    position: absolute;
    right: 34px; top: 28px;
    display: flex; align-items: center;
    color: var(--ink-dark);
  }
  .front-brand__mark {
    width: 70px; height: 70px;
    border: 3px solid var(--ink-dark);
    border-radius: 50%;
    margin-right: 16px;
  }
  .front-brand__divider {
    width: 2px; height: 82px;
    background: var(--ink-dark);
    margin-right: 14px;
  }
  .front-brand__name {
    font-family: var(--serif);
    font-weight: 400;
    font-size: 34px;
    letter-spacing: 1.5px;
    line-height: 1;
    text-transform: uppercase;
  }
  .front-brand__name small { display: block; font-size: 19px; letter-spacing: 4px; margin-top: 4px; }

  .band-grey {
    position: absolute;
    left: 0; right: 0; top: 125px; height: 150px;
    background: var(--brand-grey);
  }
  .band-orange {
    position: absolute;
    left: 0; right: 0; top: 283px; bottom: 0;
    background: var(--brand-orange);
  }

  .holder-name {
    position: absolute;
    left: 18px; top: 138px;
    color: var(--paper);
    font-family: var(--serif);
    font-weight: 700;
    font-size: 30px;
  }

  .contact {
    position: absolute;
    color: var(--paper);
    font-family: var(--sans);
    font-size: 15px;
    display: flex; align-items: center; gap: 10px;
  }
  .contact svg { flex: none; }
  .contact--phone { left: 300px; top: 200px; }
  .contact--fax { left: 455px; top: 200px; }
  .contact--address {
    left: 300px; top: 232px;
    font-family: var(--serif);
    font-size: 14px;
    line-height: 1.2;
  }
  .contact--web {
    left: 285px; top: 294px;
    font-family: var(--serif);
    font-size: 16px;
    line-height: 1.2;
  }
</style>
</head>
<body>

<section class="card card--back" aria-label="Business card, back">
  <div class="back-brand">
    <span class="back-brand__mark" aria-hidden="true"></span>
    <p class="back-brand__name">Delacourt<small>&amp; Associates</small></p>
  </div>
  <ul class="expertise">
    <li>Real Estate Development</li>
    <li>Commercial Agreements</li>
    <li>Corporate Law</li>
    <li>Franchise Agreements</li>
    <li>Financing</li>
    <li>Acquisition</li>
  </ul>
</section>

<section class="card card--front" aria-label="Business card, front">
  <div class="band-grey"></div>
  <div class="band-orange"></div>

  <div class="front-brand">
    <span class="front-brand__mark" aria-hidden="true"></span>
    <span class="front-brand__divider" aria-hidden="true"></span>
    <p class="front-brand__name">Delacourt<small>&amp; Associates</small></p>
  </div>

  <h1 class="holder-name">Marisa Delacourt</h1>

  <p class="contact contact--phone">
    <svg width="14" height="22" viewBox="0 0 14 22" aria-hidden="true">
      <rect x="1" y="1" width="12" height="20" rx="2" fill="none" stroke="#fff" stroke-width="2"/>
      <circle cx="7" cy="17" r="1.3" fill="#fff"/>
    </svg>
    514 372-5106
  </p>
  <p class="contact contact--fax">
    <svg width="20" height="20" viewBox="0 0 20 20" aria-hidden="true">
      <rect x="5" y="1" width="10" height="6" fill="#fff"/>
      <rect x="1" y="7" width="18" height="9" rx="1.5" fill="#fff"/>
      <rect x="5" y="13" width="10" height="6" fill="#fff" stroke="#58585a" stroke-width="1"/>
    </svg>
    514 372-5107
  </p>
  <p class="contact contact--address">
    <svg width="16" height="22" viewBox="0 0 16 22" aria-hidden="true">
      <path d="M8 1a7 7 0 0 0-7 7c0 5 7 13 7 13s7-8 7-13a7 7 0 0 0-7-7z" fill="#fff"/>
      <circle cx="8" cy="8" r="2.6" fill="#58585a"/>
    </svg>
    <span>Lakeshore Legal Resource Centre Inc.<br>2917 Brisebois Montreal, QC H3K 2T9</span>
  </p>
  <p class="contact contact--web">
    <svg width="22" height="22" viewBox="0 0 22 22" aria-hidden="true">
      <g fill="none" stroke="#fff" stroke-width="1.6">
        <circle cx="11" cy="11" r="9.5"/>
        <ellipse cx="11" cy="11" rx="4.2" ry="9.5"/>
        <line x1="1.5" y1="11" x2="20.5" y2="11"/>
        <line x1="3" y1="6" x2="19" y2="6"/>
        <line x1="3" y1="16" x2="19" y2="16"/>
      </g>
    </svg>
    <span>marisa@velmont-juris.ca<br>www.velmont-juris.ca</span>
  </p>
</section>

</body>
</html>
```